GIN BOTTLE LOGO NEED IT TO MATCH THE DESIGN FOR VELRA CROWN IMAGE AS THEY ARE SISTER BRANDS. I'VE ATTACHED IMAGES OF TORVIK (THE IMAGES ARE JUST FOR REFERENCE)

Logo Text

TORVIK

```html
<!DOCTYPE html>
<html lang="en">
<head>
<meta charset="UTF-8">
<title>Velra Crown &amp; Torvik Labels</title>
<link rel="stylesheet" href="https://fonts.googleapis.com/css2?family=Cinzel:wght@400;600;700&family=Cormorant+Garamond:wght@500;600&display=swap">
<style>
  :root {
    --canvas-bg: #ececec;
    --whiskey-green: #1e5530;
    --whiskey-green-deep: #174526;
    --whiskey-gold: #c9a44a;
    --whiskey-cream: #e9e7d6;
    --gin-navy: #1f2a8c;
    --gin-navy-deep: #18216f;
    --gin-cyan: #3fb6d8;
    --gin-light: #e7e9f2;
  }
  html, body {
    margin: 0;
    padding: 0;
    width: 1043px;
    height: 1200px;
    overflow: hidden;
    background: var(--canvas-bg);
  }
  .label-pair {
    width: 1043px;
    height: 1200px;
    display: flex;
    align-items: center;
    justify-content: center;
    gap: 60px;
  }
  .label {
    width: 440px;
    height: 640px;
    display: block;
  }
  .arc-title {
    font-family: "Cinzel", serif;
    font-weight: 600;
    font-size: 30px;
    letter-spacing: 2px;
  }
  .whiskey .arc-title { fill: var(--whiskey-cream); }
  .gin .arc-title { fill: var(--gin-light); letter-spacing: 5px; }
  .brand-name {
    font-family: "Cinzel", serif;
    text-anchor: middle;
  }
  .whiskey .brand-name { fill: var(--whiskey-cream); font-weight: 600; font-size: 44px; }
  .gin .brand-name { fill: var(--gin-light); font-weight: 700; font-size: 56px; letter-spacing: 4px; }
  .spec {
    font-family: "Cormorant Garamond", serif;
    font-weight: 600;
    text-anchor: middle;
  }
  .whiskey .spec { fill: var(--whiskey-cream); font-size: 15px; }
  .whiskey .spec-small { font-size: 7px; letter-spacing: 0.5px; }
  .gin .spec { fill: var(--gin-light); font-size: 17px; }
  .gin .spec-stack { font-size: 14px; letter-spacing: 1px; }
</style>
</head>
<body>
<main class="label-pair">

  <svg class="label whiskey" viewBox="0 0 440 640" aria-label="Velra Crown blended Irish whiskey label">
    <defs>
      <linearGradient id="whiskey-art-fill" x1="0" y1="0" x2="0" y2="1">
        <stop offset="0" stop-color="#cfd6c4"/>
        <stop offset="1" stop-color="#9fb39a"/>
      </linearGradient>
      <path id="whiskey-arc" d="M48,250 A172,172 0 0 1 392,250"/>
    </defs>
    <path class="label-body" d="M0,640 L0,220 A220,220 0 0 1 440,220 L440,640 Z" fill="var(--whiskey-green)"/>
    <path class="label-frame" d="M14,626 L14,220 A206,206 0 0 1 426,220 L426,626 Z" fill="none" stroke="var(--whiskey-gold)" stroke-width="2"/>
    <text class="arc-title"><textPath href="#whiskey-arc" startOffset="50%" text-anchor="middle">BLENDED IRISH WHISKEY</textPath></text>
    <path class="illustration" role="img" aria-label="Engraved portrait of a crowned goddess with flowing hair and Celtic knotwork"
          d="M95,440 L95,250 A125,125 0 0 1 345,250 L345,440 Z" fill="url(#whiskey-art-fill)"/>
    <line x1="120" y1="462" x2="320" y2="462" stroke="var(--whiskey-gold)" stroke-width="1.5"/>
    <text class="brand-name" x="220" y="512">VELRA CROWN</text>
    <rect class="ornament" role="img" aria-label="Gold scrollwork flourish" x="120" y="530" width="200" height="20" rx="10" fill="var(--whiskey-gold)" opacity="0.8"/>
    <line x1="40" y1="574" x2="400" y2="574" stroke="var(--whiskey-gold)" stroke-width="1"/>
    <text class="spec" x="95" y="604">40% ABV</text>
    <line x1="150" y1="584" x2="150" y2="616" stroke="var(--whiskey-cream)" stroke-width="1.5"/>
    <text class="spec" x="220" y="600">Triple Distilled</text>
    <text class="spec spec-small" x="220" y="612">PRODUCT OF IRELAND</text>
    <line x1="290" y1="584" x2="290" y2="616" stroke="var(--whiskey-cream)" stroke-width="1.5"/>
    <text class="spec" x="345" y="604">700 ML</text>
  </svg>

  <svg class="label gin" viewBox="0 0 440 640" aria-label="Torvik London dry gin label">
    <defs>
      <linearGradient id="gin-art-fill" x1="0" y1="0" x2="0" y2="1">
        <stop offset="0" stop-color="#2f8fbf"/>
        <stop offset="1" stop-color="#243a9c"/>
      </linearGradient>
      <path id="gin-arc" d="M50,250 A170,170 0 0 1 390,250"/>
    </defs>
    <path class="label-body" d="M0,640 L0,220 A220,220 0 0 1 440,220 L440,640 Z" fill="var(--gin-navy)"/>
    <path class="label-frame" d="M14,626 L14,220 A206,206 0 0 1 426,220 L426,626 Z" fill="none" stroke="var(--gin-cyan)" stroke-width="2"/>
    <text class="arc-title"><textPath href="#gin-arc" startOffset="50%" text-anchor="middle">LONDON DRY GIN</textPath></text>
    <path class="illustration" role="img" aria-label="Line portrait of a warrior in a fur cloak and beaded necklace before a Celtic knot arch"
          d="M85,420 L85,250 A135,135 0 0 1 355,250 L355,420 Z" fill="url(#gin-art-fill)"/>
    <rect class="ornament" role="img" aria-label="Teal tribal flourish" x="110" y="428" width="220" height="22" rx="11" fill="var(--gin-cyan)" opacity="0.75"/>
    <line x1="80" y1="462" x2="360" y2="462" stroke="var(--gin-cyan)" stroke-width="1.5"/>
    <text class="brand-name" x="220" y="522">TORVIK</text>
    <line x1="80" y1="548" x2="360" y2="548" stroke="var(--gin-cyan)" stroke-width="1.5"/>
    <path d="M220,552 L225,558 L220,564 L215,558 Z" fill="var(--gin-cyan)"/>
    <text class="spec" x="108" y="596">40% ABV</text>
    <line x1="162" y1="576" x2="162" y2="610" stroke="var(--gin-light)" stroke-width="1.5"/>
    <text class="spec spec-stack" x="222" y="588">PRODUCT OF</text>
    <text class="spec spec-stack" x="222" y="604">IRELAND</text>
    <line x1="282" y1="576" x2="282" y2="610" stroke="var(--gin-light)" stroke-width="1.5"/>
    <text class="spec" x="330" y="596">700 ML</text>
  </svg>

</main>
</body>
</html>
```